Historic Church website

We want our church website to feel warm, historic, and clean, modern, and easy to navigate. Dont use the anchor

Current website: https://www.meadowlarkfellowship.org/

Requirements
Should not have
• I would like to use the logo without the anchor

```html
<!DOCTYPE html>
<html lang="en">
<head>
<meta charset="utf-8">
<title>Meadowlark Fellowship</title>
<link rel="stylesheet" href="https://fonts.googleapis.com/css2?family=Libre+Baskerville:ital,wght@0,400;0,700;1,400&family=Montserrat:wght@400;500;600&family=Oswald:wght@400;500&display=swap">
<style>
:root{
  --dark:#2f2622;
  --dark-2:#3a2f2a;
  --cream:#ebe2d6;
  --gold:#c9a443;
  --gold-2:#d8b24a;
  --ink:#2a211d;
  --muted:#6e625a;
  --light-text:#e9dfd3;
  --faint:#b3a79c;
}
*{box-sizing:border-box;margin:0;padding:0}
html,body{width:1200px;height:4898px;overflow:hidden}
body{background:var(--cream);font-family:'Montserrat',sans-serif;color:var(--ink);position:relative}
.serif{font-family:'Libre Baskerville',serif}
section,header,footer{position:absolute;left:0;width:1200px}
.abs{position:absolute}
.photo{position:absolute;border-radius:4px}
.seal{position:absolute;border-radius:50%;background:var(--gold);border:4px solid #f2e6c4}

/* nav */
.site-nav{top:0;height:68px;background:var(--dark)}
.brand{position:absolute;top:14px;left:184px;display:flex;align-items:center;gap:10px;color:#f2e9dc;font-family:'Libre Baskerville',serif;font-size:15px}
.brand i{width:34px;height:34px;border-radius:50%;border:2px solid var(--gold);display:block}
.menu{position:absolute;top:25px;left:553px;display:flex;gap:32px;font-family:'Oswald',sans-serif;font-size:15px;letter-spacing:.5px;color:#f2e9dc}
.menu .active{color:var(--gold)}

/* hero */
.hero{top:68px;height:510px;background:linear-gradient(90deg,#1c1512 0%,#2b211b 45%,#3e3127 75%,#2a211c 100%)}
.hero h1{position:absolute;left:150px;top:144px;font-family:'Libre Baskerville',serif;font-weight:700;font-size:38px;line-height:48px;color:#fff}
.hero p{position:absolute;left:150px;top:294px;width:340px;font-size:11px;line-height:17px;color:#eee}
.btn{position:absolute;display:flex;align-items:center;justify-content:center;font-size:10px;font-weight:600;height:28px;border-radius:2px}
.btn-gold{background:var(--gold);color:var(--ink)}
.btn-line{border:1px solid var(--gold);color:var(--gold-2)}

/* verse */
.verse{top:578px;height:244px;text-align:center}
.verse blockquote{position:absolute;top:70px;left:0;width:1200px;font-family:'Libre Baskerville',serif;font-style:italic;font-size:21px;line-height:26px;color:var(--ink)}
.verse cite{position:absolute;display:block;left:0;top:140px;width:1200px;text-align:center;font-style:normal;font-size:10px;color:var(--muted)}
.verse p{position:absolute;left:0;top:196px;width:1200px;font-size:10px;color:var(--muted)}

/* about */
.about{top:822px;height:433px;background:var(--dark)}
.about h2{position:absolute;left:614px;top:80px;font-family:'Libre Baskerville',serif;font-size:24px;line-height:32px;color:#fff;font-weight:700}
.about h2 span{color:var(--gold)}
.body-copy{font-size:10.5px;line-height:15px;color:var(--faint)}
.about .body-copy{position:absolute;left:614px;top:168px;width:430px}
.about .body-copy p{margin-bottom:12px}
.link-gold{color:var(--gold);font-size:10.5px}

/* beliefs */
.beliefs{top:1255px;height:638px}
.section-title{position:absolute;left:0;width:1200px;text-align:center;font-family:'Libre Baskerville',serif;font-size:27px;color:var(--ink)}
.rule{position:absolute;left:580px;width:40px;height:1px;background:var(--gold)}
.belief{position:absolute;background:var(--dark);border-radius:4px;padding:14px;color:#eee;font-size:10.5px;line-height:13px;width:195px;height:104px;display:flex;flex-direction:column;justify-content:flex-end}
.belief svg{margin-bottom:8px}
.belief.center{text-align:center;align-items:center}

/* gather */
.gather{top:1893px;height:593px;background:linear-gradient(90deg,#2a201b,#3a2d25 50%,#2a201b)}
.gather .section-title{color:#f3ebe0}
.svc{position:absolute;top:144px;width:288px;height:329px;border-radius:3px;overflow:hidden;background:#3d302a}
.svc .photo{left:0;top:0;width:288px;height:329px;border-radius:0}
.svc-info{position:absolute;left:12px;right:12px;bottom:10px;background:rgba(50,38,32,.88);padding:10px 10px 12px;color:#ece3d7}
.svc-info h3{font-family:'Libre Baskerville',serif;font-size:11px;color:var(--gold-2);font-weight:700}
.svc-info .time{font-size:10px;margin:4px 0 8px}
.svc-info .time b{font-weight:600}
.svc-info p{font-size:11px;line-height:16px}

/* community */
.community{top:2486px;height:565px}
.community h2{position:absolute;left:0;top:52px;width:1200px;text-align:center;font-family:'Libre Baskerville',serif;font-size:27px;line-height:35px}
.community .intro{position:absolute;left:0;top:137px;width:1200px;text-align:center;font-size:11px;line-height:17px;color:var(--muted)}

/* teaching */
.teaching{top:3051px;height:432px;background:var(--dark)}
.teaching h2{position:absolute;left:150px;top:97px;font-family:'Libre Baskerville',serif;font-weight:700;font-size:24px;line-height:32px;color:#fff}
.teaching .body-copy{position:absolute;left:150px;top:188px;width:380px}
.teaching .body-copy p{margin-bottom:14px}

/* events */
.events{top:3483px;height:532px}
.events h2{position:absolute;left:635px;width:410px;top:48px;text-align:center;font-family:'Libre Baskerville',serif;font-size:27px}
.event-list{position:absolute;left:635px;top:117px;width:410px;list-style:none}
.event-list li{height:52.5px;border-bottom:1px solid #cfc3b4;display:flex;align-items:center;font-size:10.5px}
.event-list .date{width:110px;color:var(--muted)}
.event-list .name{flex:1;font-weight:600;font-size:9.5px}
.event-list .go{width:22px;height:22px;border-radius:50%;background:var(--dark);display:flex;align-items:center;justify-content:center}

/* newsletter */
.newsletter{top:4015px;height:280px;background:linear-gradient(90deg,#241b16,#3b2e25 50%,#241b16)}
.newsletter h2{position:absolute;left:0;top:70px;width:1200px;text-align:center;font-family:'Libre Baskerville',serif;font-size:27px;color:#f3ebe0;font-weight:400}
.newsletter p{position:absolute;left:0;top:122px;width:1200px;text-align:center;font-family:'Oswald',sans-serif;font-size:22px;letter-spacing:1px;color:#fff;text-transform:uppercase}
.signup{position:absolute;left:394px;top:173px;width:411px;height:39px;border-radius:20px;background:#fff;border:2px solid var(--gold);display:flex;align-items:center;padding:0 4px 0 14px;font-size:10.5px;color:#999}
.signup span{flex:1}
.signup b{background:var(--gold);color:var(--ink);font-size:9.5px;font-weight:600;border-radius:14px;padding:8px 16px}

/* review */
.review{top:4295px;height:260px}
.review h2{position:absolute;left:0;top:30px;width:1200px;text-align:center;font-family:'Libre Baskerville',serif;font-size:27px;font-weight:400}
.review blockquote{position:absolute;left:0;top:112px;width:1200px;text-align:center;font-family:'Libre Baskerville',serif;font-style:italic;font-size:17px;line-height:30px}
.review cite{position:absolute;display:block;left:0;top:182px;width:1200px;text-align:center;font-style:normal;font-size:10px;color:var(--muted)}

/* footer */
.site-footer{top:4555px;height:343px;background:var(--dark);color:var(--faint)}
.site-footer .brand{top:72px;left:150px}
.footer-about{position:absolute;left:150px;top:136px;width:180px;font-size:8.5px;line-height:12px}
.socials{position:absolute;left:150px;top:198px;display:flex;gap:12px}
.socials i{display:block;width:22px;height:22px;border-radius:50%;border:1px solid #7d6f64}
.f-col{position:absolute;top:70px;font-size:10px;line-height:19px}
.f-col h4{font-family:'Libre Baskerville',serif;font-size:11px;color:#fff;margin-bottom:4px}
.contact-row{display:flex;gap:8px;align-items:flex-start;line-height:13px;margin-bottom:8px}
.copyright{position:absolute;left:0;top:310px;width:1200px;text-align:center;font-size:8.5px;color:#8d8076;border-top:1px solid #43372f;padding-top:10px}
</style>
</head>
<body>

<header class="site-nav">
  <div class="brand"><i></i>Meadowlark Fellowship</div>
  <nav class="menu">
    <span class="active">HOME</span><span>ABOUT</span><span>BELIEFS</span><span>WORSHIP</span><span>SERMONS</span><span>CONTACT</span>
  </nav>
</header>

<section class="hero" role="img" aria-label="Dim wood-panelled library with tall bookshelves, a map and leaded windows">
  <h1>ANCIENT CHURCH.<br>ANCIENT FAITH.<br>ETERNAL TRUTH.</h1>
  <p>Rooted in Scripture, shaped by history, and faithfully proclaiming the Word of God in a changing world.</p>
  <div class="btn btn-gold" style="left:150px;top:343px;width:111px">Plan Your Visit ›</div>
  <div class="btn btn-line" style="left:291px;top:343px;width:167px">Learn About Our Church</div>
</section>

<section class="verse">
  <blockquote>"We have this hope as an anchor for the<br>soul, firm and secure."</blockquote>
  <cite>— Hebrews 6:19</cite>
  <p>A hope grounded in Christ. A faith that has endured through the ages.</p>
</section>

<section class="about">
  <div class="photo" style="left:150px;top:74px;width:407px;height:312px;background:linear-gradient(160deg,#b9c6d3 0%,#e7e3dc 40%,#cfc7bc 70%,#5a4a3a 100%)" role="img" aria-label="White stucco church building with an arched wooden door beside a palm tree"></div>
  <div class="seal" style="left:478px;top:60px;width:90px;height:90px"></div>
  <h2>A Church Anchored in the<br><span>Historic Christian</span> Faith</h2>
  <div class="body-copy">
    <p>Meadowlark Fellowship is an independent Christian church in the Protestant tradition, committed to the faithful teaching of Scripture and the preservation of historic Christian doctrine.</p>
    <p>We believe the truths of the Christian faith are not new, but ancient—received, guarded, and passed down through generations of faithful believers.</p>
    <p>Our worship, teaching, and fellowship reflect this conviction: thoughtful, reverent, and grounded in God's Word.</p>
    <p class="link-gold">Read Our Statement of Faith &nbsp;›</p>
  </div>
</section>

<section class="beliefs">
  <h2 class="section-title" style="top:82px">What We Believe</h2>
  <div class="rule" style="top:132px"></div>
  <div class="photo" style="left:486px;top:162px;width:228px;height:285px;background:radial-gradient(ellipse at center,#9a948c 0%,#78726a 55%,rgba(120,114,106,0) 75%)" role="img" aria-label="Weathered stone cross"></div>
  <div class="belief" style="left:184px;top:230px">
    <svg width="30" height="24" viewBox="0 0 30 24"><path d="M2 5h11l2 2 2-2h11v16H17l-2 2-2-2H2z" fill="#c9a443"/></svg>
    The Bible as the inspired, authoritative Word of God
  </div>
  <div class="belief" style="left:238px;top:381px">
    <svg width="30" height="30" viewBox="0 0 30 30" stroke="#c9a443" stroke-width="1.5"><path d="M15 1v28M1 15h28M5 5l20 20M25 5L5 25"/></svg>
    The Triune God: Father, Son, and Holy Spirit
  </div>
  <div class="belief" style="left:820px;top:230px">
    <svg width="32" height="24" viewBox="0 0 32 24"><path d="M2 6l7 7 7-10 7 10 7-7-3 16H5z" fill="#c9a443"/></svg>
    The Lordship of Christ over all of life
  </div>
  <div class="belief" style="left:780px;top:381px">
    <svg width="30" height="30" viewBox="0 0 30 30"><path d="M13 2l-8 16 4 10h4zM17 2l8 16-4 10h-4z" fill="#c9a443"/></svg>
    The importance of doctrinal clarity and faithful discipleship.
  </div>
  <div class="belief center" style="left:504px;top:447px;height:101px">
    <svg width="22" height="32" viewBox="0 0 22 32"><path d="M9 0h4v9h9v4h-9v19H9V13H0V9h9z" fill="#c9a443"/></svg>
    Salvation by grace alone through faith in Jesus Christ.
  </div>
  <div class="abs serif" style="top:585px;left:0;width:1200px;text-align:center;font-size:10px">Explore Our Beliefs &nbsp; →</div>
</section>

<section class="gather">
  <h2 class="section-title" style="top:57px">Gather With Us This Sunday</h2>
  <div class="svc" style="left:150px">
    <div class="photo" style="background:linear-gradient(180deg,#5a3a2a 0%,#7a5138 35%,#b09070 60%,#4a3426 100%)" role="img" aria-label="Church sanctuary with wooden beamed ceiling and arched stained windows"></div>
    <div class="svc-info"><h3>Morning Worship Service</h3><div class="time"><b>11:00 AM</b></div><p>Sunday morning worship and service takes place in the main sanctuary.</p></div>
  </div>
  <div class="svc" style="left:456px">
    <div class="photo" style="background:linear-gradient(180deg,#ece8e2 0%,#d6cec2 40%,#8a6a4c 75%,#4a3526 100%)" role="img" aria-label="Bright family room with a wall map and a wooden doorway"></div>
    <div class="svc-info"><h3>All Church Lunch</h3><div class="time"><b>12:15 PM</b> (Family Room)</div><p>Please join us for lunch after the service. Everyone is welcome!</p></div>
  </div>
  <div class="svc" style="left:762px">
    <div class="photo" style="background:linear-gradient(180deg,#2e241d 0%,#5a4432 40%,#9a7a58 60%,#3a2b21 100%)" role="img" aria-label="Two-storey library with a ladder and a large wall map"></div>
    <div class="svc-info"><h3>Afternoon Adult Bible Study</h3><div class="time"><b>12:45 PM</b> (Patio Room)</div><p>Please join us for Afternoon Adult Bible Study after the Lunch.</p></div>
  </div>
  <div class="btn btn-gold serif" style="left:514px;top:522px;width:173px;height:32px;font-weight:400;font-size:9.5px">VISIT US THIS SUNDAY</div>
</section>

<section class="community">
  <h2>A Community Formed by<br>Truth and Grace</h2>
  <div class="intro">The Christian life is lived together. We are a community shaped by shared<br>worship, thoughtful conversation, prayer, and service.<br><span style="display:block;margin-top:10px">We welcome those seeking truth, clarity, and a church rooted &nbsp;in Scripture rather than trends.</span></div>
  <div class="photo" style="left:150px;top:219px;width:900px;height:304px;border-radius:10px;background:linear-gradient(180deg,#8a5a34 0%,#cdb89a 18%,#e6dccb 50%,#c9b599 82%,#7a4e2e 100%)" role="img" aria-label="Long illustrated Bible history timeline chart laid on a wooden table"></div>
</section>

<section class="teaching">
  <h2>Faithful Teaching for the<br>Church and the World</h2>
  <div class="body-copy">
    <p>Our preaching ministry is centered on the careful exposition of Scripture explaining God's Word clearly, applying it thoughtfully, and proclaiming Christ faithfully.</p>
    <p>Each sermon seeks to instruct the mind, strengthen the conscience, and encourage believers to live under the authority of God's truth.</p>
  </div>
  <div class="btn btn-gold" style="left:150px;top:305px;width:169px">Listen to Recent Sermons</div>
  <div class="btn btn-line" style="left:334px;top:305px;width:152px">View Sermon Archive</div>
  <div class="photo" style="left:614px;top:61px;width:409px;height:312px;background:linear-gradient(160deg,#1e1712 0%,#4a3424 40%,#7a5234 60%,#2a1e16 100%)" role="img" aria-label="Study room with leather armchairs and wooden bookshelves"></div>
  <div class="seal" style="left:960px;top:312px;width:86px;height:86px"></div>
</section>

<section class="events">
  <div class="photo" style="left:0;top:0;width:593px;height:532px;border-radius:0;background:radial-gradient(ellipse at 22% 40%,#e8c98a 0%,#a8783e 18%,#5a4130 45%,#3a2c24 100%)" role="img" aria-label="Glowing lantern in softly blurred room"></div>
  <h2>Upcoming MF Event</h2>
  <ul class="event-list">
    <li><span class="date">SUN, JAN 25</span><span class="name">Plan Your Visit to MF</span><span class="go"><svg width="10" height="10" viewBox="0 0 10 10"><path d="M2 8l6-6M3 2h5v5" stroke="#fff" fill="none"/></svg></span></li>
    <li><span class="date">WED, JAN 28</span><span class="name">Wednesday Night Bible Study</span><span class="go"><svg width="10" height="10" viewBox="0 0 10 10"><path d="M2 8l6-6M3 2h5v5" stroke="#fff" fill="none"/></svg></span></li>
    <li><span class="date">SUN, FEB 01</span><span class="name">Your Visit to MF: Location, Time &amp; Parking</span><span class="go"><svg width="10" height="10" viewBox="0 0 10 10"><path d="M2 8l6-6M3 2h5v5" stroke="#fff" fill="none"/></svg></span></li>
    <li><span class="date">WED, FEB 04</span><span class="name">Wednesday Night Bible Study</span><span class="go"><svg width="10" height="10" viewBox="0 0 10 10"><path d="M2 8l6-6M3 2h5v5" stroke="#fff" fill="none"/></svg></span></li>
    <li><span class="date">SUN, FEB 08</span><span class="name">MF Visit Information</span><span class="go"><svg width="10" height="10" viewBox="0 0 10 10"><path d="M2 8l6-6M3 2h5v5" stroke="#fff" fill="none"/></svg></span></li>
    <li><span class="date">WED, FEB 11</span><span class="name">Wednesday Mid-Week Bible Study</span><span class="go"><svg width="10" height="10" viewBox="0 0 10 10"><path d="M2 8l6-6M3 2h5v5" stroke="#fff" fill="none"/></svg></span></li>
    <li><span class="date">SUN, FEB 15</span><span class="name">Visitor Information: MF</span><span class="go"><svg width="10" height="10" viewBox="0 0 10 10"><path d="M2 8l6-6M3 2h5v5" stroke="#fff" fill="none"/></svg></span></li>
  </ul>
</section>

<section class="newsletter">
  <h2>Stay Informed</h2>
  <p>Receive weekly updates, sermon notifications, and important church announcements.</p>
  <div class="signup"><span>Enter Your Email</span><b>SUBMIT</b></div>
</section>

<section class="review">
  <h2>Review</h2>
  <blockquote>"Christians are called to God's service not only in church<br>professions but also in every secular calling."</blockquote>
  <cite class="serif">— Elias Warrington</cite>
</section>

<footer class="site-footer">
  <div class="brand"><i></i>Meadowlark Fellowship</div>
  <p class="footer-about">Meadowlark Fellowship seeks to glorify God through faithful worship, sound doctrine, and the proclamation of the gospel of Jesus Christ.</p>
  <div class="socials"><i></i><i></i><i></i></div>
  <div class="f-col" style="left:724px">
    <h4>Quick Links</h4>
    Home<br>About<br>Beliefs<br>Worship<br>Sermons<br>Contact
  </div>
  <div class="f-col" style="left:843px;width:220px">
    <h4>Contact Us</h4>
    <div class="contact-row"><svg width="10" height="12" viewBox="0 0 10 12"><path d="M5 11S1 7 1 4.5a4 4 0 018 0C9 7 5 11 5 11z" stroke="#c9a443" fill="none"/><circle cx="5" cy="4.5" r="1.3" fill="#c9a443"/></svg><span>2240 Larkspur Avenue<br>Fairhaven, California 90000</span></div>
    <div class="contact-row"><svg width="11" height="9" viewBox="0 0 11 9"><rect x=".5" y=".5" width="10" height="8" stroke="#c9a443" fill="none"/><path d="M.5.5l5 4 5-4" stroke="#c9a443" fill="none"/></svg><span>info@meadowlarkfellowship.org</span></div>
    <div class="contact-row"><svg width="10" height="10" viewBox="0 0 10 10"><path d="M2 1l2 2-1 1.5a6 6 0 002.5 2.5L7 6l2 2-1.5 1.5C4 9 1 6 .5 2.5z" fill="#c9a443"/></svg><span>555 014 2287</span></div>
  </div>
  <div class="copyright serif">© Copyright 2026 &nbsp;| &nbsp;Meadowlark Fellowship, Fairhaven, California. All Rights Reserved.</div>
</footer>

</body>
</html>
```